Lend a Lantern Website Design (design layout only)

We need a website design for a new nonprofit organization based in Des Moines, Iowa called Lend a Lantern. The nonprofit provides soccer training opportunities to youth soccer players looking to improve their game while also affecting the lives of the less fortunate in a positive way. While participating in the training programs the players also go out and raise money for selected charities. The organization then donates the funds. In its first 18 months we donated $10,500. We would like to see designs attempt to symbolize the mission of the nonprofit - essentially "improve you while improving someone else."

We would like to see the following features:

· A place to donate - Our intent is to have the home page linked to the donation page; a simple straight-forward process for people to give money, and make donating as painless as possible - no account needed to make a donation, credit card or e-check should be the only information needed to donate, and have it be on a single page.

· A photo gallery so people can browse the photo gallery to get a better understanding of our organization and a place to add videos and a calendar to show upcoming events

· A place for contact information and the profiles of directors and board members. This should include a spot showing all the charities the organization donates to. Also includes a news section/blog for comments and suggestions.

We want the design to revolve around the content and mission. We would really like to stress our organization as nonprofit. We would also like if the website was user friendly and easy to navigate.

The logo of our organization is uploaded

```html
<!DOCTYPE html>
<html lang="en">
<head>
<meta charset="utf-8">
<title>Lend a Lantern</title>
<link href="https://fonts.googleapis.com/css2?family=Arimo:wght@400;700&family=Open+Sans:wght@400;600;700&display=swap" rel="stylesheet">
<style>
:root{
  --green:#4f6b34;
  --green-text:#4a6f2c;
  --brand:#6a9a3a;
  --ink:#1a1a1a;
  --body:#222;
  --rule:#d9d9d9;
  --footer:#1f1f1f;
  --footer-base:#121212;
  --grey:#8c8c8c;
}
*{margin:0;padding:0;box-sizing:border-box}
html,body{width:856px;height:1200px;overflow:hidden;background:#fff}
body{position:relative;font-family:Arimo,Arial,sans-serif;color:var(--body)}
.abs{position:absolute}

/* header */
.brand{left:73px;top:30px;width:140px;font-family:"Open Sans",sans-serif;font-weight:700;font-size:22px;line-height:24px;color:var(--brand);display:flex;align-items:center;gap:8px}
.brand-dot{width:16px;height:16px;border-radius:50%;background:var(--brand);flex:none}
.helpline{right:81px;top:39px;font-size:14px;color:var(--green-text);display:flex;align-items:center;gap:5px}
.helpline .num{color:var(--grey)}
.donate{left:582px;top:70px;width:201px;height:40px;border:2px solid #000;border-radius:6px;background:linear-gradient(#111 0,#000 55%,#222 100%);box-shadow:inset 0 0 0 2px #fff;color:#fff;font-family:"Open Sans",sans-serif;font-weight:600;font-size:20px;display:flex;align-items:center;justify-content:center;text-decoration:none}

/* nav */
.topline{left:0;top:124px;width:856px;height:3px;background:#111}
.nav{left:0;top:127px;width:856px;height:36px;background:var(--green)}
.nav ul{list-style:none;position:absolute;left:73px;top:4px;display:flex;height:28px}
.nav li{font-size:10.4px;color:#fff;display:flex;align-items:center;padding:0 14px;border-left:1px solid #2f441c;box-shadow:inset 1px 0 0 #6b8a4c}
.nav li:first-child{border:none;box-shadow:none;background:#000;width:84px;justify-content:center;margin-right:16px}
.nav li:nth-child(2){padding:0 15px}

/* hero */
.hero{left:0;top:163px;width:856px;height:287px;background:linear-gradient(100deg,#c9ccd3 0%,#aab3c2 30%,#9aa5b8 55%,#7a7470 75%,#d8d2cc 100%)}
.hero-caption{left:88px;top:302px;width:324px;height:70px;background:rgba(20,20,20,.88);font-family:"Open Sans",sans-serif;font-weight:600;padding:6px 0 0 24px}
.hero-caption .t1{color:#fff;font-size:22px;line-height:28px}
.hero-caption .t2{color:var(--brand);font-size:20px;line-height:28px}

/* main */
.main{left:73px;top:470px;width:460px}
.main h1{font-family:Arimo,Arial,sans-serif;font-weight:400;font-size:20px;color:var(--ink);margin-bottom:14px}
.main h2{font-family:Arimo,Arial,sans-serif;font-weight:400;font-size:17.5px;color:var(--green-text);margin:20px 0 14px}
.main p{font-size:10px;line-height:15.6px;margin-bottom:16px}
.news{display:flex;gap:11px;margin-left:-2px}
.news-photo{width:116px;height:78px;flex:none;margin-top:2px}
.news p{margin:0;font-size:10px;line-height:15.6px}
.news a{color:#000;text-decoration:none}
.news-sep{border-top:1px dotted #bbb;margin:28px 0 30px}

/* sidebar */
.side{left:561px;top:472px;width:213px}
.side h3{font-family:"Open Sans",sans-serif;font-weight:700;font-size:15.5px;letter-spacing:.6px;color:#222}
.bar{height:3px;margin:11px 0 7px;background:linear-gradient(90deg,#000 0 32px,var(--green) 32px)}
.side ul{list-style:none;margin-bottom:20px}
.side li{font-size:9.6px;padding:6px 0 7px 16px;border-bottom:1px dotted #ccc;margin-right:6px;position:relative}
.side li:last-child{border:none}
.side li::before{content:"";position:absolute;left:4px;top:9px;border-left:4px solid #000;border-top:3.5px solid transparent;border-bottom:3.5px solid transparent}
.gallery-photo{width:213px;height:131px;border:2px solid #ccc;background:linear-gradient(160deg,#3e5a2e,#6c8d4a 50%,#2f4324)}

/* footer */
.footer{left:0;top:1049px;width:856px;height:124px;background:var(--footer)}
.foot-base{left:0;top:1173px;width:856px;height:27px;background:var(--footer-base);color:#ddd;font-size:8.5px;text-align:center;line-height:27px}
.divider{top:1064px;height:100px;border-left:1px dotted #555}
.addr{left:137px;top:1089px;width:117px;text-align:right;color:#eee;font-size:8.6px;line-height:13px}
.addr .name{font-family:"Open Sans",sans-serif;font-weight:700;font-size:12.5px;letter-spacing:.4px;color:#fff;margin-bottom:2px}
.addr a{display:block;color:#ddd;margin-top:5px;text-decoration:underline}
.follow{left:360px;top:1089px;width:150px;text-align:center;color:#eee;font-family:"Open Sans",sans-serif;font-weight:700;font-size:12.5px;letter-spacing:.5px}
.social{left:398px;top:1119px;display:flex;gap:8px}
.social span{width:28px;height:28px;border-radius:50%;background:#2e5a9a;border:2px solid #d6d6d6}
.social span+span{background:#3c9ad6}
.foot-brand{left:630px;top:1120px;width:100px;text-align:center;font-family:"Open Sans",sans-serif;font-weight:700;font-size:16px;line-height:18px;color:#555}
</style>
</head>
<body>

<header>
  <div class="abs brand"><span class="brand-dot"></span><span>LEND A<br>LANTERN</span></div>
  <div class="abs helpline">For Help Call
    <svg width="12" height="12" viewBox="0 0 24 24" aria-hidden="true"><path fill="#4a6f2c" d="M6.6 10.8a15.1 15.1 0 0 0 6.6 6.6l2.2-2.2a1 1 0 0 1 1-.25 11.4 11.4 0 0 0 3.6.57 1 1 0 0 1 1 1V20a1 1 0 0 1-1 1A17 17 0 0 1 3 4a1 1 0 0 1 1-1h3.5a1 1 0 0 1 1 1c0 1.25.2 2.45.57 3.57a1 1 0 0 1-.25 1z"/></svg>
    <span class="num">555.204.7731</span></div>
  <a class="abs donate" href="#">Donate Now</a>
</header>

<div class="abs topline"></div>
<nav class="abs nav">
  <ul>
    <li>HOME</li><li>WHO WE ARE</li><li>TRAINING</li><li>BOARD OF DIRECTORS</li><li>BOARD MEMBERS</li><li>GALLERY</li><li>CONTACT</li>
  </ul>
</nav>

<section class="abs hero" role="img" aria-label="Youth women's soccer players chasing a ball on a field"></section>
<div class="abs hero-caption">
  <div class="t1">A Non Profit Orgnisation</div>
  <div class="t2">Learn While Helping Others</div>
</div>

<main class="abs main">
  <h1>WHAT WE DO</h1>
  <p>The nonprofit provides soccer training opportunities to youth soccer players looking to improve their game while also affecting the lives of the less fortunate in a positive way. While participating in the training programs the players also go out and raise money for selected charities. The organization then donates the funds. In its first 18 months we donated $10,500.</p>
  <h2>Our Mission</h2>
  <p>The nonprofit provides soccer training opportunities to youth soccer players looking to improve their game while also affecting the lives of the less fortunate in a positive way.</p>
  <p>While participating in the training programs the players also go out and raise money for selected charities. The organization then donates the funds. In its first 18 months we donated $10,500.</p>
  <h2>Latest News</h2>
  <div class="news">
    <div class="news-photo" role="img" aria-label="Girls playing soccer on a sunny field" style="background:linear-gradient(180deg,#b9c7d6,#8a9aa8 50%,#5f7f3a)"></div>
    <p>The nonprofit provides soccer training opportunities to youth soccer players looking to improve their game while also affecting the lives of the less fortunate in a positive way. While participating in the training programs the players also go out and raise money for selected charities. The organization then donates the funds. In its first 18 months we donated $10,500. &nbsp;<a href="#">Read More...</a></p>
  </div>
  <div class="news-sep"></div>
  <div class="news">
    <div class="news-photo" role="img" aria-label="Young boys competing for the ball in green kits" style="background:linear-gradient(180deg,#6f7f58,#4d7a3a 55%,#3f6a2c)"></div>
    <p>The nonprofit provides soccer training opportunities to youth soccer players looking to improve their game while also affecting the lives of the less fortunate in a positive way. While participating in the training programs the players also go out and raise money for selected charities. The organization then donates the funds. In its first 18 months we donated $10,500. &nbsp;<a href="#">Read More...</a></p>
  </div>
</main>

<aside class="abs side">
  <h3>Upcoming Events</h3>
  <div class="bar"></div>
  <ul>
    <li>Robotic competitions teach students</li>
    <li>Robotic competitions teach students how to</li>
    <li>Robotic competitions teach</li>
    <li>Robotic competitions teach students</li>
    <li>Robotic competitions teach</li>
  </ul>
  <h3>Our Charities</h3>
  <div class="bar"></div>
  <ul>
    <li>In its first 18 months $5000</li>
    <li>In its first 18 months we donated $10,500</li>
    <li>n its first 18 months $5000</li>
    <li>In its first 18 months we donated $10,500</li>
    <li>In its first 18 months $5000</li>
  </ul>
  <h3>Our Gallery</h3>
  <div class="bar"></div>
  <div class="gallery-photo" role="img" aria-label="Two professional players contesting the ball in a stadium"></div>
</aside>

<footer>
  <div class="abs footer"></div>
  <svg class="abs" style="left:80px;top:1088px" width="32" height="44" viewBox="0 0 32 44" aria-hidden="true"><path fill="#9a9a9a" d="M16 0C7.2 0 0 7.2 0 16c0 11 16 28 16 28s16-17 16-28C32 7.2 24.8 0 16 0zm0 22a6 6 0 1 1 0-12 6 6 0 0 1 0 12z"/></svg>
  <div class="abs addr">
    <div class="name">LEND A LANTERN</div>
    18 Harlow Lane,<br>Maple Grove 3021
    <a href="#">Click here to see the directions &gt;&gt;</a>
  </div>
  <div class="abs divider" style="left:318px"></div>
  <div class="abs follow">Follow Us On:</div>
  <div class="abs social"><span></span><span></span></div>
  <div class="abs divider" style="left:539px"></div>
  <div class="abs foot-brand">LEND A<br>LANTERN</div>
  <div class="abs foot-base">Copyright © 2015 Lend a Lantern. All Rights Reserved.</div>
</footer>

</body>
</html>
```